Harborline Capital Inc. Investor Presentation

We would like a PowerPoint presentation to attract prospective investors. It needs to look extremely professional since we are a financial lending institution, and seeking capital investors. We specialize in Private Lending with Mortgage Backed Securities, both Residential and Commercial properties.

```html
<!DOCTYPE html>
<html lang="en">
<head>
<meta charset="utf-8">
<title>Harborline Capital – Investor Presentation</title>
<link rel="stylesheet" href="https://fonts.googleapis.com/css2?family=Cormorant+Garamond:wght@500&family=Poppins:wght@600&family=Archivo:wght@700&family=Open+Sans:wght@400&display=swap">
<style>
  :root{
    --mat:#e0e0e0;
    --white:#ffffff;
    --navy:#232865;
    --gold:#e8c53f;
    --gold-deep:#d9b53a;
    --photo-blue:#6c70a8;
    --photo-violet:#8b86ad;
    --photo-cream:#d9d39a;
    --ink:#111111;
    --chart-navy:#1f4a7a;
    --bar:#33506f;
    --bar-alt:#9a9a9a;
    --rule:#a9a58a;
    --grid:#d6d6d6;
  }
  *{box-sizing:border-box;margin:0;padding:0}
  html,body{width:1200px;height:750px;overflow:hidden;background:var(--mat)}
  .board{position:relative;width:1200px;height:750px}
  .slide{position:absolute;width:515px;height:290px;background:var(--white);overflow:hidden}
  .slide--cover{left:76px;top:71px}
  .slide--about{left:630px;top:71px}
  .slide--chart{left:76px;top:381px}
  .slide--contact{left:630px;top:381px;background:var(--gold)}
  .layer{position:absolute;left:0;top:0}

  .wordmark{position:absolute;font-family:"Cormorant Garamond",serif;font-weight:500;color:var(--ink);text-align:center;line-height:1;letter-spacing:1px}
  .wordmark span{display:block;margin-bottom:2px}
  .slide--cover .wordmark{left:235px;top:132px;width:260px;font-size:33px}
  .tagline{position:absolute;left:233px;top:244px;width:282px;height:20px;font-family:"Archivo",sans-serif;font-weight:700;font-size:12.5px;color:var(--ink);display:flex;align-items:center;justify-content:center;letter-spacing:.3px}

  .about-photo{position:absolute;left:0;top:0;width:130px;height:290px;background:linear-gradient(160deg,var(--photo-cream),#c7b77a 60%,#8d8a6c)}
  .gold-bar{position:absolute;top:0;width:7px;height:290px;background:var(--gold)}
  .ornament{position:absolute;width:66px;height:66px}
  .about-copy{position:absolute;left:147px;top:26px;width:350px;display:flex;flex-direction:column}
  .about-text{font-family:"Poppins",sans-serif;font-weight:600;font-size:9.3px;line-height:15.4px;color:var(--ink);letter-spacing:-.05px}
  .about-text--intro{text-align:left}
  .about-text--record{text-align:justify;margin-top:27px}
  .about-rule{width:249px;height:1px;margin:5px 0 0 5px;background:var(--gold)}

  .chart-photo{position:absolute;left:0;top:0;width:82px;height:290px;background:linear-gradient(170deg,#9b97b8,var(--photo-violet) 50%,#6f6b93)}
  .chart-title{position:absolute;left:130px;top:50px;width:321px;text-align:center;font-family:"Open Sans",sans-serif;font-weight:400;font-size:11.5px;color:var(--chart-navy);letter-spacing:.3px}
  .chart-rule{position:absolute;left:130px;top:68px;width:321px;height:1.5px;background:var(--rule)}
  .chart{position:absolute;left:0;top:0}
  .chart text{font-family:"Open Sans",sans-serif;fill:#222}
  .corner-name{position:absolute;left:435px;top:251px;width:70px;font-family:"Cormorant Garamond",serif;font-weight:500;font-size:8px;line-height:8px;color:var(--navy);text-align:center}

  .contact-photo{position:absolute;inset:0;background:radial-gradient(ellipse at 50% 35%,#ebcd55,var(--gold) 45%,var(--gold-deep) 100%)}
  .slide--contact .wordmark{left:129px;top:112px;width:258px;font-size:27px;color:var(--ink)}
  .address{position:absolute;left:60px;top:225px;width:396px;text-align:center;font-family:"Poppins",sans-serif;font-weight:600;font-size:9.8px;line-height:15.6px;color:var(--ink)}
</style>
</head>
<body>
<main class="board">

  <section class="slide slide--cover">
    <svg class="layer" width="515" height="290" viewBox="0 0 515 290">
      <polygon points="0,0 281,0 167,235 0,235" fill="var(--photo-blue)" role="img" aria-label="Glass office tower photograph in blue-violet tone"/>
      <polygon points="115,0 127,0 46,167 36,167" fill="var(--white)"/>
      <polygon points="138,0 152,0 102,115 93,115" fill="var(--white)"/>
      <polygon points="210,134 218,134 162,235 158,235" fill="var(--white)"/>
      <polyline points="0,137 54,26 238,26 123,260 0,260" fill="none" stroke="var(--gold)" stroke-width="1.2"/>
    </svg>
    <div class="wordmark"><span>HARBORLINE</span><span>CAPITAL</span></div>
    <svg class="layer" width="515" height="290" viewBox="0 0 515 290">
      <polygon points="218,264 233,244 515,244 515,264" fill="var(--gold)"/>
    </svg>
    <div class="tagline">PERFORM - PROTECT - PROSPER</div>
  </section>

  <section class="slide slide--about">
    <div class="about-photo" role="img" aria-label="Photograph of a hand writing on financial papers beside a laptop"></div>
    <div class="gold-bar" style="left:130px"></div>
    <div class="ornament" style="left:100px;top:205px;background:rgba(35,40,101,.12)" role="img" aria-label="Decorative diamond ornament"></div>
    <div class="about-copy">
      <p class="about-text about-text--intro">Harborline Capital is a leading private investor and business accelerator that leverages the experience, insights, and resources of its founder, Mr. Daniel R. Whitcombe, an accomplished entrepreneur and investor.</p>
      <div class="about-rule"></div>
      <p class="about-text about-text--record">Harborline Capital has been investing its own capital since 1998 and has had a prestigious track record generating over $2 Billion in enterprise value across various industries including financial services, software, biotechnology, advanced manufacturing, and alternative energy.</p>
    </div>
  </section>

  <section class="slide slide--chart">
    <div class="chart-photo" role="img" aria-label="Photograph of pens, coins and banknotes in violet tone"></div>
    <div class="gold-bar" style="left:82px"></div>
    <div class="ornament" style="left:55px;top:212px;background:rgba(232,197,63,.25)" role="img" aria-label="Decorative diamond ornament"></div>
    <h2 class="chart-title">LONG-TERM DEBT MATURITY PROFILE</h2>
    <div class="chart-rule"></div>
    <svg class="chart" width="515" height="290" viewBox="0 0 515 290">
      <text x="133" y="106" font-size="6.5">($MM)</text>
      <g stroke="var(--grid)" stroke-width=".6">
        <line x1="159" y1="114" x2="449" y2="114"/>
        <line x1="159" y1="132" x2="449" y2="132"/>
        <line x1="159" y1="150" x2="449" y2="150"/>
        <line x1="159" y1="168" x2="449" y2="168"/>
        <line x1="159" y1="186" x2="449" y2="186"/>
      </g>
      <line x1="159" y1="204" x2="449" y2="204" stroke="#888" stroke-width=".7"/>
      <g font-size="6.3" text-anchor="end">
        <text x="151" y="116">1,250</text><text x="151" y="134">1,000</text>
        <text x="151" y="152">750</text><text x="151" y="170">500</text>
        <text x="151" y="188">250</text><text x="151" y="206">0</text>
      </g>
      <g fill="var(--bar)">
        <rect x="198.5" y="186" width="6" height="18"/>
        <rect x="207.8" y="182.4" width="6" height="21.6"/>
        <rect x="217.2" y="186" width="6" height="18"/>
        <rect x="226.6" y="182.4" width="6" height="21.6"/>
        <rect x="245.3" y="171.6" width="6" height="32.4"/>
        <rect x="282.8" y="189.6" width="6" height="14.4"/>
        <rect x="301.5" y="186" width="6" height="18"/>
        <rect x="310.9" y="193.2" width="6" height="10.8"/>
        <rect x="357.7" y="182.4" width="6" height="21.6"/>
        <rect x="367.1" y="173.4" width="6" height="30.6"/>
        <rect x="385.8" y="186" width="6" height="18"/>
        <rect x="395.2" y="168" width="6" height="36"/>
        <rect x="404.5" y="178.8" width="6" height="25.2"/>
        <rect x="423.3" y="182.4" width="6" height="21.6"/>
        <rect x="432.6" y="160.8" width="6" height="43.2"/>
        <rect x="442" y="132" width="6" height="72"/>
      </g>
      <rect x="207.8" y="146.4" width="6" height="36" fill="var(--bar-alt)"/>
      <g font-size="4" text-anchor="middle">
        <text x="164" y="211">2020</text><text x="183" y="211">2022</text><text x="201" y="211">2024</text>
        <text x="220" y="211">2026</text><text x="239" y="211">2028</text><text x="258" y="211">2030</text>
        <text x="276" y="211">2032</text><text x="295" y="211">2034</text><text x="314" y="211">2036</text>
        <text x="333" y="211">2038</text><text x="351" y="211">2040</text><text x="370" y="211">2042</text>
        <text x="389" y="211">2044</text><text x="408" y="211">2046</text><text x="426" y="211">2048</text>
        <text x="445" y="211">2050</text>
      </g>
      <rect x="225" y="218" width="3.5" height="3.5" fill="var(--bar)"/>
      <text x="231" y="222" font-size="6.5">HLC Long-Term Debt</text>
      <rect x="312" y="218" width="3.5" height="3.5" fill="var(--bar-alt)"/>
      <text x="318" y="222" font-size="6.5">HLP Long-Term Debt</text>
    </svg>
    <div class="corner-name">HARBORLINE<br>CAPITAL</div>
  </section>

  <section class="slide slide--contact">
    <div class="contact-photo" role="img" aria-label="Photograph of office tower facades in golden tone"></div>
    <div class="wordmark"><span>HARBORLINE</span><span>CAPITAL</span></div>
    <p class="address">Lakeview Plaza, North Harbour Tower<br>240 Front Street, Suite 1450 Toronto, ON M5V 1A8<br>Tel: 416-555-0148</p>
  </section>

</main>
</body>
</html>
```